Business card for a new innovative and professional lawn care business

We need a business card design for a new lawn care business in Halifax NS Canada. We offer lawn services in Halifax & Bedford. Our services offered include lawn care, garden services, and property maintenance. We take pride in our work and are experienced at what we do. I would like to see a design that is double sided. On the backside I would like the something simple (maybe my logo preferably on blackround (linked below) with website link, Leafbook page or something). The front I want to include contact info:
Marcus Dell
phone 902-415-3968
email - brookvaleyards.ca
facebook - Leafbook.com/brookvaleyards
Picshare maybe ? - picshare.com/brookvaleyard
Serving Halifax and Bedford for 5 years?
I don't want it to have too much information as I will be passing them out in aim to visit website, or call !
We do want it to include lawn care, garden services and property maintenance.
Basic, catchy, and modern looking !
Logo attached below !

Target Market(s)

Passing business cards to everyone I meet or interact with.

Industry/Entity Type

Lawn Care

Contact Information for Business Card

Double sided with some basic information, with catchy colours and easy to look at.

Font styles to use
Sans Serif

Requirements
Must have
• Must be double sided and have :
• Name, Phone, Email, FB, Website, and 3 main services offered - lawn care, property maintenance, garden services
Nice to have
• Would be nice to have instagram link if it goes well on there
Should not have
• Don't want too much writing or images that are distracting

```html
<!DOCTYPE html>
<html lang="en">
<head>
<meta charset="utf-8">
<title>Brookvale Yards – Business Card</title>
<link href="https://fonts.googleapis.com/css2?family=Open+Sans:wght@400;600;700;800&display=swap" rel="stylesheet">
<style>
  :root {
    --canvas: #e9ebe8;
    --lime: #8cc63f;
    --forest: #1f6b2e;
    --white: #ffffff;
    --ink: #1c1c1c;
    --panel: #f3f4f2;
    --divider: #d9dcd6;
  }
  * { box-sizing: border-box; margin: 0; padding: 0; }
  html, body {
    width: 1200px; height: 900px; overflow: hidden;
    background: var(--canvas);
    font-family: "Open Sans", Arial, sans-serif;
  }
  .stage { position: relative; width: 1200px; height: 900px; }
  .card {
    position: absolute; width: 560px; height: 320px;
    border-radius: 22px; overflow: hidden;
    box-shadow: 0 10px 28px rgba(0,0,0,0.18);
  }
  .brand {
    position: absolute; display: flex; align-items: center;
    font-weight: 800; text-transform: uppercase; letter-spacing: 1px;
    white-space: nowrap;
  }
  .brand-mark { border-radius: 50%; background: var(--forest); flex: none; }

  /* back side */
  .card-back { left: 120px; top: 100px; background: var(--lime); }
  .card-back .brand {
    left: 0; right: 0; top: 112px; justify-content: center; gap: 14px;
    color: var(--white); font-size: 38px;
  }
  .card-back .brand-mark { width: 18px; height: 18px; }
  .social {
    position: absolute; left: 40px; right: 40px; bottom: 34px;
    display: flex; gap: 28px; color: var(--white); font-size: 15px; font-weight: 600;
  }
  .social-item { display: flex; align-items: center; gap: 8px; white-space: nowrap; }
  .social-square { width: 13px; height: 13px; background: var(--forest); border-radius: 2px; flex: none; }

  /* front side */
  .card-front { left: 520px; top: 470px; background: var(--white); }
  .contact-panel { position: absolute; top: 0; right: 0; width: 250px; height: 100%; }
  .card-front .brand {
    left: 36px; top: 176px; gap: 10px;
    color: var(--lime); font-size: 22px;
  }
  .card-front .brand-mark { width: 13px; height: 13px; }
  .contact { position: absolute; left: 330px; top: 42px; color: var(--ink); }
  .person {
    color: var(--lime); font-weight: 800; font-size: 24px;
    text-transform: uppercase; line-height: 1.1; margin-bottom: 6px;
  }
  .contact-line {
    display: flex; align-items: center; gap: 8px;
    font-size: 14.5px; font-weight: 600; line-height: 1.45; white-space: nowrap;
  }
  .contact-line svg { width: 12px; height: 12px; flex: none; }
  .services-title {
    margin-top: 12px; color: var(--lime); font-weight: 800;
    font-size: 19px; text-transform: uppercase;
  }
  .services { list-style: none; }
  .services li {
    display: flex; align-items: center; gap: 8px;
    font-size: 15px; font-weight: 600; line-height: 1.4; white-space: nowrap;
  }
  .services li::before {
    content: ""; width: 7px; height: 7px; border-radius: 50%;
    background: var(--lime); flex: none;
  }
</style>
</head>
<body>
<main class="stage">
  <section class="card card-back" aria-label="Card back">
    <div class="brand"><span class="brand-mark"></span>Brookvale Yards</div>
    <div class="social">
      <span class="social-item"><span class="social-square"></span>Leafbook.com/brookvaleyards</span>
      <span class="social-item"><span class="social-square"></span>picshare.com/brookvaleyard</span>
    </div>
  </section>

  <section class="card card-front" aria-label="Card front">
    <svg class="contact-panel" viewBox="0 0 250 320" preserveAspectRatio="none" aria-hidden="true">
      <polygon points="40,0 250,0 250,320 90,320 0,150" fill="var(--panel)"/>
      <polyline points="40,0 0,150 90,320" fill="none" stroke="var(--divider)" stroke-width="1.5"/>
    </svg>
    <div class="brand"><span class="brand-mark"></span>Brookvale Yards</div>
    <div class="contact">
      <p class="person">Marcus Dell</p>
      <p class="contact-line">
        <svg viewBox="0 0 12 12"><path d="M2.5 1h2l1 2.5-1.3 1a6 6 0 0 0 3.3 3.3l1-1.3L11 7.5v2A1.5 1.5 0 0 1 9.5 11 8.5 8.5 0 0 1 1 2.5 1.5 1.5 0 0 1 2.5 1z" fill="var(--lime)"/></svg>
        902-415-3968</p>
      <p class="contact-line">
        <svg viewBox="0 0 12 12"><rect x="1" y="2.5" width="10" height="7" rx="1" fill="none" stroke="var(--lime)" stroke-width="1.3"/><path d="M1.5 3l4.5 3.5L10.5 3" fill="none" stroke="var(--lime)" stroke-width="1.3"/></svg>
        info@brookvaleyards.ca</p>
      <p class="contact-line">
        <svg viewBox="0 0 12 12"><circle cx="6" cy="6" r="4.8" fill="none" stroke="var(--lime)" stroke-width="1.2"/><ellipse cx="6" cy="6" rx="2" ry="4.8" fill="none" stroke="var(--lime)" stroke-width="1"/><path d="M1.2 6h9.6" stroke="var(--lime)" stroke-width="1"/></svg>
        www.brookvaleyards.ca</p>
      <p class="services-title">Services</p>
      <ul class="services">
        <li>Lawn care</li>
        <li>Garden services</li>
        <li>Property maintenance</li>
      </ul>
    </div>
  </section>
</main>
</body>
</html>
```